Modern, eye catching eliquid bottle label. 1.5 x 2.75

We need a label design for our e-juice bottles. The labels to be printed are 1.5 inches in height and 2.75 inches in width. We are looking to include our website (www.quillbrookmistparlor.com) and our phone number of 2 different shops. The most prominent thing needs to be our logo(attached .pdf and jpeg). We will need 2 spots that we can edit on an ongoing basis for nicotine strength and the flavor. We want something simplistic but eye-catching. Our colors are Purple, Red, and Orange. We would also like our website fairly prominent as well.

Target Market(s)

18-45 vapers and e-cigarette users

Font styles to use
Serif

Colors
6b449b
f78e1f
ec1f27
ffffff
000000

Requirements
Must have
• eye catching
• "Quillbrook Mist" must be LARGE
• phone number
• website
• areas for flavor name and nicotine strength
• orange, purple, black and red
Nice to have
• clean, abstract vectors
• "corporate look"
• think of a JUNO FIZZ can, you immediately know what your'e looking at.
• Our V in vapor is our go to logo
Should not have
• no grunge effects
• no round shapes

```html
<!DOCTYPE html>
<html lang="en">
<head>
<meta charset="utf-8">
<title>Quillbrook Mist – E-Liquid Label</title>
<link href="https://fonts.googleapis.com/css2?family=Roboto+Condensed:wght@300;400&family=Parisienne&display=swap" rel="stylesheet">
<style>
  :root {
    --purple: #6b449b;
    --purple-deep: #55288a;
    --purple-light: #8a4fb8;
    --orange: #f78e1f;
    --orange-light: #f9a825;
    --red: #ec1f27;
    --red-orange: #e8502a;
    --white: #ffffff;
    --ink: #1c1c1c;
    --brand-ink: #5d2a8c;
  }
  * { box-sizing: border-box; margin: 0; padding: 0; }
  html, body { width: 1200px; height: 655px; overflow: hidden; background: var(--white); }
  .label {
    position: relative;
    width: 1200px;
    height: 655px;
    background: var(--white);
    font-family: "Roboto Condensed", "Arial Narrow", sans-serif;
    font-weight: 300;
    color: var(--white);
  }
  .band { position: absolute; }
  .band--purple {
    background: linear-gradient(135deg, var(--purple-light) 0%, var(--purple) 45%, var(--purple-deep) 100%);
  }
  .band--left-top { left: 0; top: 0; width: 318px; height: 235px; }
  .band--left-mid { left: 0; top: 235px; width: 318px; height: 270px;
    background: linear-gradient(90deg, var(--orange-light) 0%, var(--orange) 100%); }
  .band--left-bottom { left: 0; top: 505px; width: 318px; height: 150px; }
  .band--right-top { left: 861px; top: 0; width: 339px; height: 235px; }
  .band--right-mid { left: 861px; top: 235px; width: 339px; height: 270px;
    background: linear-gradient(90deg, var(--orange) 0%, var(--red-orange) 60%, var(--red) 100%); }
  .band--right-bottom { left: 861px; top: 505px; width: 339px; height: 150px; }

  .text { position: absolute; font-size: 30px; line-height: 1.2; white-space: nowrap; }
  .nicotine { left: 36px; top: 52px; }
  .flavours-heading { left: 36px; top: 252px; }
  .flavours-list { left: 36px; top: 316px; list-style: none; line-height: 44px; font-size: 31px; }
  .mfg-date { left: 36px; top: 533px; }
  .exp-date { left: 36px; top: 586px; }

  .warning { left: 903px; top: 30px; font-size: 27px; line-height: 36px; white-space: normal; width: 280px; }
  .ingredients { left: 903px; top: 276px; font-size: 27px; line-height: 36px; white-space: normal; width: 280px; }
  .location { left: 903px; font-size: 30px; }
  .location--one { top: 530px; }
  .location--two { top: 583px; }

  .brand-name {
    position: absolute; left: 318px; width: 543px; top: 160px;
    text-align: center; font-size: 66px; font-weight: 400; color: var(--purple);
    white-space: nowrap;
  }
  .flavour-name {
    position: absolute; left: 318px; width: 543px; top: 300px;
    text-align: center; font-family: "Parisienne", cursive; font-size: 140px;
    color: var(--brand-ink); line-height: 1.1;
  }
  .volume {
    position: absolute; left: 727px; top: 503px; width: 60px; height: 60px;
    border: 2px solid var(--ink); border-radius: 50%;
    display: flex; align-items: center; justify-content: center;
    color: var(--ink); font-size: 25px; font-weight: 400;
  }
  .website {
    position: absolute; left: 318px; width: 543px; top: 598px;
    text-align: center; font-size: 30px; font-weight: 400; color: var(--ink);
  }
</style>
</head>
<body>
  <main class="label">
    <div class="band band--purple band--left-top"></div>
    <div class="band band--left-mid"></div>
    <div class="band band--purple band--left-bottom"></div>
    <div class="band band--purple band--right-top"></div>
    <div class="band band--right-mid"></div>
    <div class="band band--purple band--right-bottom"></div>

    <p class="text nicotine">Nicotine Level</p>
    <p class="text flavours-heading">Other Flavours:</p>
    <ul class="text flavours-list">
      <li>Sample Flavour1</li>
      <li>Sample Flavour2</li>
      <li>Sample Flavour3</li>
      <li>Sample Flavour4</li>
    </ul>
    <p class="text mfg-date">Mfg Date:</p>
    <p class="text exp-date">Exp Date:</p>

    <h1 class="brand-name">Quillbrook Mist</h1>
    <h2 class="flavour-name">Flavour</h2>
    <div class="volume">15ml</div>
    <p class="website">www.quillbrookmistparlor.com</p>

    <p class="text warning">Warning: Please keep out of children’s reach; keep in a cool, dark place or in the refrigerator for extended life;</p>
    <p class="text ingredients">Ingredients: USP Glycerine, USP Propylene Glycol, Natural and Artificial Flavoring</p>
    <p class="text location location--one">Location 1: 214-555-0187</p>
    <p class="text location location--two">Location 2: 214-555-0187</p>
  </main>
</body>
</html>
```